Informational Website for MOSVALEK-MOSaic VALley Eastern Kinship of Clinic Record Scholars

I need an informational website to help establish us as a legitimate entity. This will help us as we seek funding in to perform the research we intend to carry out. We are a newly formed group of family physicians and primary care researchers from 9 different countries around the world. We have access to electronic medical record data and/or health insurance claims data in our respective countries. We intend to perform international comparative studies in primary care. Our set of projects are to study the impact of the COVID-19 pandemic on primary care in our respective countries and around the world.
I've already purchased a domain and website from Wix. It is a premium account. The domain is https://www.mosvalekclinicnet.org

Target Market(s)

Researchers, policy makers, universities, research funding agencies

Coding

Coded - Design and coding required

Number of Pages Required

5+ page

Font styles to use
Sans Serif

Requirements
Must have
• Must have our logo and an interactive map of the world highlighting Canada, Australia, China (including Hong Kong), Norway, Singapore, South Korea, Sweden, United Kingdom, United States.
This map must be editable such that we can add or remove countries and cities as we evolve. Please see attached brief.
Nice to have
• Nice to depict primary care and big data research

```html
<!DOCTYPE html>
<html lang="en">
<head>
<meta charset="utf-8">
<title>MOSVALEK – MOSaic VALley Eastern Kinship of Clinic Record Scholars</title>
<link rel="stylesheet" href="https://fonts.googleapis.com/css2?family=Montserrat:wght@300;400;500;600;700&family=Open+Sans:wght@400;600&display=swap">
<style>
:root{
  --green:#7aa80e;
  --green-dark:#6a950a;
  --navy:#0c2d7a;
  --navy-deep:#062068;
  --white:#ffffff;
  --ink:#222428;
  --muted:#7b7f86;
  --grey-bg:#f2f3f4;
  --map:#e7e8ea;
}
*{box-sizing:border-box;margin:0;padding:0}
html,body{width:1200px;height:4267px;overflow:hidden;background:var(--white)}
body{position:relative;font-family:"Open Sans",Arial,sans-serif;color:var(--ink)}
h1,h2,h3{font-family:"Montserrat",Arial,sans-serif}

/* header */
.site-header{position:absolute;left:0;top:0;width:1200px;height:95px;background:var(--white)}
.brand{position:absolute;left:80px;top:26px;display:flex;align-items:center;gap:10px}
.brand-dot{width:44px;height:44px;border-radius:50%;background:var(--green)}
.brand-name{font-family:"Montserrat",sans-serif;font-weight:700;font-size:24px;color:var(--navy);letter-spacing:.5px}
.main-nav{position:absolute;left:358px;top:40px;display:flex;gap:28px;font-family:"Montserrat",sans-serif;font-size:12.5px;color:#7a7d84}
.main-nav .active{color:var(--ink);font-weight:600}

/* hero */
.hero{position:absolute;left:0;top:95px;width:1200px;height:515px;background:linear-gradient(120deg,#0b1f3e 0%,#1d4a7a 40%,#2c6a9c 60%,#10284a 100%)}
.hero-title{position:absolute;left:133px;top:120px;font-size:82px;font-weight:400;color:var(--white);line-height:1}
.hero-sub{position:absolute;left:133px;top:208px;width:760px;font-family:"Montserrat",sans-serif;font-size:35px;line-height:50px;color:var(--white);font-weight:400}
.btn{display:inline-block;font-family:"Montserrat",sans-serif;font-size:13.5px;font-weight:500;color:var(--white);text-align:center}
.hero-btn{position:absolute;left:133px;top:332px;width:165px;height:38px;line-height:38px;background:var(--green)}
.hero-dots{position:absolute;left:133px;top:385px;display:flex;gap:5px}
.hero-dots span{width:15px;height:15px;border:2px solid var(--white);border-radius:50%}

/* feature circles */
.feature{position:absolute;border-radius:50%;color:var(--white);text-align:center;display:flex;flex-direction:column;align-items:center}
.feature h3{font-size:23px;font-weight:700;margin:12px 0 8px;letter-spacing:.3px}
.feature p{font-size:13px;line-height:15px;width:200px}
.feature-pub{left:133px;top:585px;width:288px;height:288px;background:var(--green);padding-top:48px}
.feature-grants{left:776px;top:585px;width:288px;height:288px;background:var(--green);padding-top:48px}
.feature-pres{left:415px;top:502px;width:370px;height:370px;background:var(--navy);border:10px solid var(--white);padding-top:78px;z-index:2}

/* about */
.about{position:absolute;left:0;top:959px;width:1200px;height:544px;background:linear-gradient(100deg,#86b216 0%,#7aa80e 50%,#6f9d09 100%)}
.about-photo{position:absolute;left:133px;top:101px;width:382px;height:295px;background:linear-gradient(135deg,#0f2744,#2a5d8a 55%,#163356)}
.about-badge{position:absolute;left:355px;top:285px;width:145px;height:145px;border-radius:50%;background:var(--white);border:6px solid var(--white)}
.about-badge::after{content:"";position:absolute;inset:10px;border-radius:50%;border:5px solid var(--ink)}
.about h2{position:absolute;left:595px;top:104px;font-size:38px;font-weight:400;color:var(--white)}
.about .rule{position:absolute;left:595px;top:159px;width:72px;height:3px;background:var(--white)}
.about-text{position:absolute;left:595px;top:186px;width:470px;font-size:13.3px;line-height:31.6px;color:var(--white)}
.about-btn{position:absolute;left:595px;top:408px;width:155px;height:36px;line-height:36px;background:var(--navy)}

/* what we do */
.section-title{position:absolute;left:0;width:1200px;text-align:center;font-family:"Montserrat",sans-serif;font-size:36px;font-weight:400}
.title-rule{position:absolute;left:564px;width:72px;height:4px}
.services-title{top:1545px;color:var(--navy)}
.services-title b{font-weight:500}
.service{position:absolute;border-radius:50%;text-align:center}
.service h3{font-size:24px;font-weight:400;margin-bottom:14px}
.service p{font-size:13.5px;line-height:25px;margin:0 auto}
.service-primary{left:110px;top:1700px;width:310px;height:318px;border:2px solid var(--navy);padding-top:122px}
.service-primary h3,.service-data h3{color:var(--ink)}
.service-primary p,.service-data p{color:var(--muted);width:200px}
.service-data{left:776px;top:1696px;width:310px;height:314px;border:2px solid var(--navy);padding-top:126px}
.service-family{left:405px;top:1662px;width:388px;height:388px;background:var(--green);padding-top:148px;color:var(--white);z-index:2}
.service-family h3{font-size:28px}
.service-family p{width:240px;font-size:15.5px;line-height:29px}
.icon-ring{position:absolute;border-radius:50%;background:var(--white);display:flex;align-items:center;justify-content:center;z-index:3}
.icon-ring .core{border-radius:50%;display:flex;align-items:center;justify-content:center}

/* partners */
.partners{position:absolute;left:0;top:2101px;width:1200px;height:419px;background:var(--navy)}
.partners h2{position:absolute;left:0;top:86px;width:1200px;text-align:center;font-size:29px;font-weight:400;color:var(--white)}
.partners h2 b{font-weight:700}
.partners .rule{position:absolute;left:564px;top:143px;width:72px;height:4px;background:var(--white)}
.partner-row{position:absolute;left:120px;top:225px;width:960px;height:60px;display:flex;align-items:center;justify-content:space-between}
.partner{display:flex;align-items:center;gap:8px;font-family:"Montserrat",sans-serif;font-size:19px;font-weight:500;color:var(--white);white-space:nowrap}
.partner .mark{width:20px;height:20px;border:2px solid var(--white);border-radius:50%}
.carousel-arrow{position:absolute;top:2322px}

/* location */
.location-title{top:2573px;color:var(--ink)}
.location-title b{font-weight:700}
.world-map{position:absolute;left:91px;top:2676px;width:1044px;height:530px;border-radius:40px;background:radial-gradient(ellipse at 40% 45%,#eceded 0%,#e3e4e6 60%,#f4f4f5 100%)}
.pin{position:absolute;width:22px;height:30px}

/* contact */
.contact{position:absolute;left:0;top:3269px;width:1200px;height:691px;background:linear-gradient(110deg,#7eab10 0%,#76a30d 50%,#6d9a0a 100%)}
.contact-ring{position:absolute;left:121px;top:119px;width:464px;height:464px;border-radius:50%;border:14px solid rgba(255,255,255,.22)}
.contact-photo{position:absolute;left:159px;top:157px;width:388px;height:388px;border-radius:50%;background:linear-gradient(140deg,#cfd8e0 0%,#3b6a92 45%,#0f2a48 100%)}
.contact h2{position:absolute;left:671px;top:101px;font-size:37px;font-weight:700;color:var(--white)}
.contact h2 span{font-weight:400}
.contact-form{position:absolute;left:671px;top:176px;width:447px}
.field{height:42px;border-radius:21px;background:var(--white);margin-bottom:16px;font-size:11px;color:#555;padding:13px 18px;position:relative}
.field.textarea{height:110px;border-radius:24px}
.field.select svg{position:absolute;right:18px;top:15px}
.submit{height:42px;border-radius:21px;background:var(--navy);color:var(--white);font-family:"Montserrat",sans-serif;font-weight:700;font-size:14px;text-align:center;line-height:42px;margin-top:22px}

/* footer */
.site-footer{position:absolute;left:0;top:3960px;width:1200px;height:307px;background:var(--grey-bg)}
.footer-brand{position:absolute;left:0;top:60px;width:1200px;display:flex;justify-content:center;align-items:center;gap:14px}
.footer-brand .brand-dot{width:70px;height:70px}
.footer-brand .brand-name{font-size:40px}
.footer-nav{position:absolute;left:0;top:168px;width:1200px;display:flex;justify-content:center;gap:22px;font-family:"Montserrat",sans-serif;font-size:13.5px;color:#555}
.copyright{position:absolute;left:0;top:198px;width:1200px;text-align:center;font-family:"Montserrat",sans-serif;font-size:13px;color:#444;font-weight:500}
.social{position:absolute;left:533px;top:232px;display:flex;gap:5px}
.social span{width:28px;height:28px;border-radius:50%;border:2px solid var(--ink);background:var(--white)}
</style>
</head>
<body>

<header class="site-header">
  <div class="brand"><span class="brand-dot"></span><span class="brand-name">MOSVALEK</span></div>
  <nav class="main-nav">
    <span class="active">HOME</span><span>ABOUT US</span><span>PARTICIPATION INSITUTION</span><span>PUBLICATION</span><span>PRESENTATION</span><span>GRANTS</span><span>NEWS</span>
  </nav>
</header>

<section class="hero" role="img" aria-label="Researchers working at computer screens showing world data in a control room">
  <h1 class="hero-title">MOSVALEK</h1>
  <p class="hero-sub">MOSaic VALley Eastern Kinship of Clinic Record Scholars</p>
  <span class="btn hero-btn">READ MORE</span>
  <div class="hero-dots"><span></span><span></span><span></span><span></span></div>
</section>

<div class="feature feature-pub">
  <svg width="64" height="44" viewBox="0 0 64 44" fill="none" stroke="#fff" stroke-width="4"><rect x="4" y="3" width="56" height="38" rx="3"/><line x1="14" y1="14" x2="50" y2="14"/><line x1="14" y1="23" x2="50" y2="23"/><line x1="14" y1="32" x2="50" y2="32"/></svg>
  <h3>PUBLICATIONS</h3>
  <p>Lorem ipsum dolor sit amet, consectetur adipiscing elit, sed do eiusmod tempor</p>
</div>
<div class="feature feature-pres">
  <svg width="62" height="58" viewBox="0 0 62 58" fill="none" stroke="#fff" stroke-width="3"><rect x="24" y="4" width="34" height="26" rx="2"/><line x1="31" y1="12" x2="51" y2="12"/><line x1="31" y1="19" x2="45" y2="19"/><circle cx="12" cy="12" r="6"/><path d="M4 54V30q0-8 8-8h6l10 6M12 38v16M20 54V34"/></svg>
  <h3>PRESENTATION</h3>
  <p>Lorem ipsum dolor sit amet, consectetur adipiscing elit, sed do eiusmod tempor incididunt ut labore et dolore.</p>
</div>
<div class="feature feature-grants">
  <svg width="48" height="64" viewBox="0 0 48 64" fill="none" stroke="#fff" stroke-width="3"><rect x="6" y="4" width="36" height="56" rx="3"/><circle cx="24" cy="18" r="7"/><line x1="13" y1="34" x2="35" y2="34"/><line x1="13" y1="42" x2="35" y2="42"/><line x1="13" y1="50" x2="28" y2="50"/></svg>
  <h3>GRANTS</h3>
  <p>Lorem ipsum dolor sit amet, consectetur adipiscing elit, sed do eiusmod tempor</p>
</div>

<section class="about">
  <div class="about-photo" role="img" aria-label="Researcher analysing medical data on several monitors"></div>
  <div class="about-badge" role="img" aria-label="Globe with stethoscope emblem"></div>
  <h2>ABOUT MOSVALEK</h2>
  <span class="rule"></span>
  <p class="about-text">We are family physicians and primary care researchers from 9 different countries around the world. We have access to electronic medical record data and/or health insurance claims data in our respective countries. We intend to perform international comparative studies in primary care. Our first project is to study the impact of the COVID-19 pandemic on primary care in our</p>
  <span class="btn about-btn">READ MORE</span>
</section>

<h2 class="section-title services-title"><b>WHAT</b> WE DO</h2>
<span class="title-rule" style="top:1598px;background:var(--green)"></span>

<div class="icon-ring" style="left:206px;top:1663px;width:124px;height:124px;border:2px solid var(--navy)">
  <div class="core" style="width:110px;height:110px;background:var(--green)">
    <svg width="52" height="46" viewBox="0 0 52 46" fill="none" stroke="#fff" stroke-width="3"><path d="M22 4h8v8h8v8h-8v8h-8v-8h-8v-8h8z"/><path d="M4 32h10l8 4h10q4 0 4 4H18M4 42h26l16-10"/></svg>
  </div>
</div>
<div class="service service-primary">
  <h3>PRIMARY CARE</h3>
  <p>Lorem ipsum dolor sit amet, consectetur adipiscing elit, sed do eiusmod tempor</p>
</div>

<div class="service service-family">
  <h3>FAMILY MEDICINE</h3>
  <p>Lorem ipsum dolor sit amet, consectetur adipiscing elit, sed do eiusmod tempor</p>
</div>
<div class="icon-ring" style="left:516px;top:1620px;width:160px;height:160px;border:2px solid var(--green)">
  <div class="core" style="width:140px;height:140px;background:var(--navy)">
    <svg width="56" height="62" viewBox="0 0 56 62" fill="none" stroke="#fff" stroke-width="3"><path d="M8 4h26l10 10v22M8 4v52h22"/><circle cx="24" cy="24" r="8"/><line x1="24" y1="19" x2="24" y2="29"/><line x1="19" y1="24" x2="29" y2="24"/><line x1="14" y1="40" x2="30" y2="40"/><circle cx="42" cy="48" r="9"/><circle cx="50" cy="54" r="5"/></svg>
  </div>
</div>

<div class="icon-ring" style="left:862px;top:1663px;width:124px;height:124px;border:2px solid var(--navy)">
  <div class="core" style="width:110px;height:110px;background:var(--green)">
    <svg width="52" height="50" viewBox="0 0 52 50" fill="none" stroke="#fff" stroke-width="3"><rect x="14" y="4" width="34" height="30" rx="2"/><line x1="22" y1="26" x2="22" y2="20"/><line x1="30" y1="26" x2="30" y2="14"/><line x1="38" y1="26" x2="38" y2="10"/><circle cx="14" cy="32" r="8"/><line x1="8" y1="38" x2="2" y2="46"/></svg>
  </div>
</div>
<div class="service service-data">
  <h3>DATA RESEARCH</h3>
  <p>Lorem ipsum dolor sit amet, consectetur adipiscing elit, sed do eiusmod tempor</p>
</div>

<section class="partners">
  <h2><b>PARTICIPATING</b> INSTITUTIONS</h2>
  <span class="rule"></span>
  <div class="partner-row">
    <span class="partner">Ashgrove Health Trust</span>
    <span class="partner">Kestrel Data Lab</span>
    <span class="partner"><span class="mark"></span>Fernvale County</span>
    <span class="partner">Tidewater Clinic Network</span>
  </div>
</section>
<svg class="carousel-arrow" style="left:30px" width="22" height="38" viewBox="0 0 22 38" fill="none" stroke="#fff" stroke-width="4"><path d="M18 4L4 19l14 15"/></svg>
<svg class="carousel-arrow" style="left:1148px" width="22" height="38" viewBox="0 0 22 38" fill="none" stroke="#fff" stroke-width="4"><path d="M4 4l14 15L4 34"/></svg>

<h2 class="section-title location-title">OUR <b>LOCATION</b></h2>
<span class="title-rule" style="top:2626px;background:var(--navy)"></span>
<div class="world-map" role="img" aria-label="World map highlighting member countries"></div>
<svg width="0" height="0" style="position:absolute"><defs><symbol id="pin" viewBox="0 0 22 30"><path d="M11 30C4 20 1 15 1 10a10 10 0 0 1 20 0c0 5-3 10-10 20z" fill="#0c2d7a"/><circle cx="11" cy="10" r="4" fill="#fff"/></symbol></defs></svg>
<svg class="pin" style="left:224px;top:2770px"><use href="#pin"/></svg>
<svg class="pin" style="left:301px;top:2785px"><use href="#pin"/></svg>
<svg class="pin" style="left:554px;top:2742px"><use href="#pin"/></svg>
<svg class="pin" style="left:579px;top:2716px"><use href="#pin"/></svg>
<svg class="pin" style="left:604px;top:2716px"><use href="#pin"/></svg>
<svg class="pin" style="left:965px;top:2804px"><use href="#pin"/></svg>
<svg class="pin" style="left:937px;top:2853px"><use href="#pin"/></svg>
<svg class="pin" style="left:915px;top:2911px"><use href="#pin"/></svg>
<svg class="pin" style="left:1015px;top:3095px"><use href="#pin"/></svg>

<section class="contact">
  <div class="contact-ring"></div>
  <div class="contact-photo" role="img" aria-label="Data scientist working at multiple monitors"></div>
  <h2>CONTACT <span>US</span></h2>
  <form class="contact-form">
    <div class="field">Full Name*</div>
    <div class="field">Email*</div>
    <div class="field">Phone No.*</div>
    <div class="field select">You are interested in*<svg width="12" height="8" viewBox="0 0 12 8" fill="none" stroke="#333" stroke-width="2"><path d="M1 1l5 5 5-5"/></svg></div>
    <div class="field textarea">Message</div>
    <div class="submit">SUBMIT NOW</div>
  </form>
</section>

<footer class="site-footer">
  <div class="footer-brand"><span class="brand-dot"></span><span class="brand-name">MOSVALEK</span></div>
  <nav class="footer-nav"><span>HOME</span><span>ABOUT US</span><span>PARTICIPATION INSITUTION</span><span>PUBLICATION</span><span>PRESENTATION</span><span>GRANTS</span><span>NEWS</span></nav>
  <p class="copyright">© 2021 Pinecroft Studio &nbsp;All Rights Reserved</p>
  <div class="social" aria-label="Social links"><span></span><span></span><span></span><span></span></div>
</footer>

</body>
</html>
```